BEACON CABS

Taxi card design

Need changes very slow in replying to my messages.

Target Market(s)

Customers

Industry/Entity Type

Taxi

Contact Information for Business Card

See previous design

Font styles to use
Sans Serif

Colors
A7469A
B969AE
D3A5CF
EDDBEB
F8F0F9
6B429C
8869AF
B7A5CE
E3DAEB
F3F0F8

Requirements
Nice to have
• We are in the business of looking after people, not just driving vehicles front
Should not have
• Front number 01632 480 480 needs to big big

```html
<!DOCTYPE html>
<html lang="en">
<head>
<meta charset="utf-8">
<title>Beacon Cabs – Business Card</title>
<link rel="stylesheet" href="https://fonts.googleapis.com/css2?family=Bebas+Neue&family=Saira:wght@800&display=swap">
<style>
  :root {
    --page: #ffffff;
    --card: #f1eef5;
    --ink: #080808;
    --magenta: #ab1785;
    --plum: #4e066b;
    --indigo: #25005f;
    --white: #ffffff;
  }
  html, body {
    margin: 0;
    padding: 0;
    width: 1200px;
    height: 720px;
    overflow: hidden;
    background: var(--page);
  }
  .canvas {
    position: relative;
    width: 1200px;
    height: 720px;
  }
  .card {
    position: absolute;
    left: 40px;
    top: 40px;
    width: 1120px;
    height: 640px;
    background: var(--card);
    overflow: hidden;
  }
  .corner {
    position: absolute;
    width: 200px;
    height: 98px;
  }
  .corner--top-left {
    left: 0;
    top: 0;
    background: linear-gradient(90deg, var(--plum), var(--magenta));
    border-bottom-right-radius: 100px 70px;
  }
  .corner--bottom-right {
    right: 0;
    bottom: 0;
    background: linear-gradient(90deg, var(--magenta), var(--plum));
    border-top-left-radius: 100px 70px;
  }
  .brand-name {
    position: absolute;
    left: 0;
    right: 0;
    top: 216px;
    margin: 0;
    text-align: center;
    font-family: "Saira", sans-serif;
    font-weight: 800;
    font-size: 106px;
    line-height: 1;
    letter-spacing: 2px;
    color: var(--ink);
  }
  .phone-pill {
    position: absolute;
    left: 179px;
    top: 396px;
    width: 743px;
    height: 98px;
    border-radius: 49px;
    background: linear-gradient(90deg, var(--magenta), var(--indigo));
    overflow: hidden;
  }
  .phone-icon {
    position: absolute;
    left: 45px;
    top: 20px;
    width: 30px;
    height: 58px;
  }
  .phone-number {
    position: absolute;
    left: 105px;
    top: 50%;
    transform: translateY(-50%);
    display: flex;
    gap: 12px;
    font-family: "Bebas Neue", sans-serif;
    font-size: 72px;
    line-height: 1;
    letter-spacing: 26px;
    color: var(--white);
    white-space: nowrap;
  }
  .phone-number span:last-child {
    letter-spacing: 26px;
    margin-right: -26px;
  }
</style>
</head>
<body>
  <div class="canvas">
    <section class="card">
      <div class="corner corner--top-left"></div>
      <div class="corner corner--bottom-right"></div>

      <h1 class="brand-name">BEACON CABS</h1>

      <div class="phone-pill">
        <svg class="phone-icon" viewBox="0 0 30 58" aria-hidden="true">
          <defs>
            <linearGradient id="handsetShade" x1="0" y1="0" x2="1" y2="0">
              <stop offset="0" stop-color="#25005f"/>
              <stop offset="1" stop-color="#ab1785"/>
            </linearGradient>
          </defs>
          <path d="M15 0 L18 16 L14 17 L17 40 L21 39 L25 58 C20 59 16 58 13 54 C5 44 0 28 2 8 C4 3 9 1 15 0 Z" fill="url(#handsetShade)"/>
        </svg>
        <div class="phone-number">
          <span>01632</span><span>480</span><span>480</span>
        </div>
      </div>
    </section>
  </div>
</body>
</html>
```